Geschäftspapiere für Kanzlei
Zielgruppe
Forschungsinstitute und Großunternehmen die eigene Entwicklungsabteilungen haben und Erfindungen patentieren lassen.
Aufgabenstellung
Möglicherweise ergibt eine Weiterentwiklung unseres logos Sinn? Denkbar wäre für uns aber auch auf das Logo ganz zu verzichten.
Es sollte nicht mehr als eine Farbe (Blauton) verwendet werden. Wir wollen schlicht, klassisch und seriös auftreten.

```html
<!DOCTYPE html>
<html lang="de">
<head>
<meta charset="utf-8">
<title>Briefbogen Kanzlei Dr. Korinthi</title>
<link href="https://fonts.googleapis.com/css2?family=Libre+Franklin:wght@400;500&display=swap" rel="stylesheet">
<style>
  :root {
    --backdrop: #d4d4d6;
    --paper: #ecebef;
    --brand-blue: #18223f;
    --ink: #141414;
  }
  * { margin: 0; padding: 0; box-sizing: border-box; }
  html, body {
    width: 959px; height: 1200px; overflow: hidden;
    background: var(--backdrop);
  }
  .letterhead {
    position: absolute; left: 73px; top: 20px;
    width: 812px; height: 1160px;
    background: var(--paper);
    font-family: "Libre Franklin", Arial, sans-serif;
    color: var(--ink);
  }
  .brand {
    position: absolute; left: 63px; top: 84px;
    display: flex; align-items: center; gap: 12px;
    color: var(--brand-blue);
    font-weight: 500; font-size: 21px; letter-spacing: 0.04em;
  }
  .brand-square { width: 18px; height: 18px; background: var(--brand-blue); }
  .sender-details {
    position: absolute; left: 560px; top: 66px;
    font-size: 11.3px; line-height: 15.6px;
  }
  .sender-details p + p { margin-top: 15.6px; }
  .return-address {
    position: absolute; left: 63px; top: 258px;
    font-size: 13.4px; white-space: nowrap;
  }
  .return-address .sep { margin: 0 5px; }
  .legal-footer {
    position: absolute; left: 0; right: 0; top: 1110px;
    text-align: center; font-size: 11.9px; line-height: 15.6px;
  }
</style>
</head>
<body>
  <div class="letterhead">
    <div class="brand">
      <span class="brand-square"></span>
      <span class="brand-name">DR. TAMAZ KORINTHI</span>
    </div>

    <div class="sender-details">
      <p>Dr. rer. nat. Tamaz Korinthi, PhD<br>Patentanwalt<br>European Patent Attorney<br>European Design- und Trademark Attorney</p>
      <p>Lindenhofstrasse 22<br>80339 München</p>
      <p>Tel.: + 49 89 318 406 270<br>Fax: + 49 89 777 312 65<br>Email: office@korinthi-ip.de</p>
    </div>

    <div class="return-address">
      Kanzlei Dr. Korinthi<span class="sep">•</span>Lindenhofstrasse 22<span class="sep">•</span>80339 München
    </div>

    <div class="legal-footer">
      Patentanwaltskanzlei Dr. Korinthi, Steuernummer.: 143/258/61937, www.korinthi-ip.de<br>
      Südstadt Kreditbank SKB, UStID Nummer, IBAN: DE02100500009988776655, BIC: SKBKDEM1XXX
    </div>
  </div>
</body>
</html>
```